Information poster for parquet showroom

We are a parquet shop from germany and need some information poster for our showroom, to show our costumers some important information about parqut directly. The three posters are about reasons for parquet, and there are two types of paper on the subject. We would like to place the posters in a wooden frame. The design should be modern but simple. Enclosed I send you some of my ideas but it does not have to be like this. Can be completely different. I also send you some pictures of our showroom. 1st poster: Why parquet (dimension: 90x130 cm) Why parquet? - brings nature into your home - ecologically sustainable raw material - pleasantly warm - timeless% 26amp; high quality optics - durable% 26amp; reparable flooring - improved indoor climate - unique ride 2. Advantages oiled - tangible wood structure - natural appearance - scratches less present - partial repair possible advantage varnished - very easy-care - classic% 26amp; elegant appearance - protection against dirt and moisture - variable gloss level 3. Poster: overview of the hardness of different kinds of wood (dimension: 67x130 cm) wood hardness according to Brinell in N / mm² maple europ. 28 maple canadian. 35 birch 27 beech 33 oak 34 alder 17 ash 37 doussie 42 spruce 12 kambala 30 chestnut 18 pine 20 cherry european. 31 Larch 19 Merbau 44 Robinia 48 Sucupira 57 Elm 30 Wenge 45

```html
<!DOCTYPE html>
<html lang="de">
<head>
<meta charset="utf-8">
<title>Warum Parkett?</title>
<link rel="stylesheet" href="https://fonts.googleapis.com/css2?family=Bebas+Neue&display=swap">
<style>
  :root {
    --backdrop: #d2d3d1;
    --paper: #ffffff;
    --ink: #111111;
    --accent: #ff7a00;
    --wood-light: #ddd7cf;
    --wood-mid: #cbc3b9;
    --wood-dark: #b9b0a5;
    --band-shadow: #8f8a84;
  }
  * { box-sizing: border-box; margin: 0; padding: 0; }
  html, body { width: 1200px; height: 801px; overflow: hidden; }
  body {
    background: var(--backdrop);
    font-family: "Bebas Neue", "Arial Narrow", sans-serif;
    position: relative;
  }
  .poster {
    position: absolute;
    left: 320px; top: 22px;
    width: 560px; height: 757px;
    background: var(--paper);
    overflow: hidden;
  }
  .header-visual {
    position: absolute;
    left: 16px; top: 20px;
    width: 226px; height: 174px;
    background: radial-gradient(ellipse at 50% 60%, #dca66e 0%, #e8bf8c 45%, #f6f1ea 75%, #ffffff 100%);
  }
  .title {
    position: absolute;
    right: 28px;
    text-align: right;
    line-height: 1;
  }
  .title-main {
    top: 24px;
    font-size: 122px;
    letter-spacing: 4px;
    color: var(--ink);
  }
  .title-sub {
    top: 126px;
    font-size: 72px;
    letter-spacing: 2px;
    color: var(--accent);
  }
  .title-sub .mark { color: var(--ink); margin-left: 14px; }
  .wood-field {
    position: absolute;
    left: 0; top: 210px;
    width: 560px; height: 547px;
    background:
      linear-gradient(180deg, rgba(255,255,255,0.15), rgba(0,0,0,0.04)),
      linear-gradient(90deg, var(--wood-light) 0%, var(--wood-mid) 35%, var(--wood-light) 60%, var(--wood-dark) 100%);
  }
  .reasons { list-style: none; }
  .reason {
    position: absolute;
    height: 48px;
    background: var(--paper);
    font-size: 31px;
    line-height: 48px;
    color: var(--ink);
    padding-left: 34px;
    white-space: nowrap;
  }
  .reason::after {
    content: "";
    position: absolute;
    left: 16px; right: 16px; bottom: -7px;
    height: 7px;
    background: var(--band-shadow);
    opacity: 0.7;
  }
  .reason.left { left: 4px; width: 470px; }
  .reason.right { left: 105px; width: 455px; }
  .reason em { font-style: normal; color: var(--accent); }
</style>
</head>
<body>
  <main class="poster">
    <div class="header-visual" role="img" aria-label="Stapel heller Parkettdielen aus Holz"></div>
    <h1>
      <span class="title title-main">Warum</span>
      <span class="title title-sub">Parkett<span class="mark">?</span></span>
    </h1>
    <div class="wood-field" role="img" aria-label="Heller grau-beiger Holzdielenboden als Hintergrund"></div>
    <ul class="reasons">
      <li class="reason left" style="top:254px">Holt die <em>Natur</em> in Ihr Zuhause</li>
      <li class="reason right" style="top:336px"><em>Ökologisch</em> nachhaltiger Rohstoff</li>
      <li class="reason left" style="top:417px">Angenehm <em>fußwarm</em></li>
      <li class="reason right" style="top:498px"><em>Zeitlose</em> &amp; hochwertige Optik</li>
      <li class="reason left" style="top:579px">Langlebiger &amp; <em>reparabler</em> Bodenbelag</li>
      <li class="reason right" style="top:659px">Einzigartiges <em>Laufgefühl</em></li>
    </ul>
  </main>
</body>
</html>
```